FoldKite App for On-Demand Laundry

We are launching a startup of online laundry service using mobile app. This startup will give the most convenient experience for the customers in managing their laundry. In only few taps away with the app, we'll send our agents to pick up laundry at the customer's doorstep, proceed it as per their order type, and get it delivered back to them in a schedule that fits them well.

We need somebody that can help with us and make our app as one of the simplest yet most effective app to use, design should be clean and easy to navigate, leave experience that makes our users want to come back and use it again. It will consist of key features that the app should have as follows:

- Sign up & Login
- Add customer address
- Schedule laundry pick up & delivery
- Laundry service selection
- Confirmation and Payment
- Status Tracking

Please refer to the attachment for details of business flows. Example of apps that can inspire: Rinsely, Sudzoria, Presqo.

--PLEASE DO NOT USE THE LOGO FROM ATTACHMENT, IT'S ONLY A DUMMY LOGO--
Updates

Target Market(s)

Young Professional, College Students, Young Early Family

Industry/Entity Type

Cleaning Service

Font styles to use
Sans Serif

Colors
ffffff
9d9d9d
0392cd
33a6d7
86cfc6
33b8a4
acd036
cadf82

Requirements
Must have
• Simplicity and elegance. Clean and easy navigation.
• Example from attachment is "ugly" but can tell the overall idea on what information to capture from the app. We need to get a completely different design which is way better than it.
Nice to have
• Inspiration could be from similar apps like: Rinsely, Sudzoria, and Presqo.
Should not have
• --PLEASE DO NOT USE THE LOGO FROM ATTACHMENT, IT'S ONLY A DUMMY LOGO--

```html
<!DOCTYPE html>
<html lang="en">
<head>
<meta charset="utf-8">
<title>FoldKite – App Screens</title>
<link href="https://fonts.googleapis.com/css2?family=Roboto:ital,wght@0,300;0,400;0,500;1,300&display=swap" rel="stylesheet">
<style>
:root{
  --bg:#f0f0f0;
  --white:#ffffff;
  --teal:#04a690;
  --teal-soft:#33b8a4;
  --blue:#33a6d7;
  --ink:#333333;
  --grey:#9d9d9d;
  --line:#dcdcdc;
}
*{margin:0;padding:0;box-sizing:border-box}
html,body{width:1200px;height:1080px;overflow:hidden}
body{background:var(--bg);font-family:"Roboto",Helvetica,Arial,sans-serif;color:var(--ink);position:relative}
.screen{position:absolute;width:275px;height:490px;background:var(--white);overflow:hidden;box-shadow:0 1px 4px rgba(0,0,0,.12)}
.abs{position:absolute}
.status{position:absolute;top:0;left:0;right:0;height:16px;font-size:8.5px;display:flex;justify-content:space-between;align-items:center;padding:0 5px;color:#111}
.status .time{font-weight:500}
.center{left:0;right:0;text-align:center}
.header-title{top:29px;font-size:13px;color:#444}
.close{left:20px;top:28px}
.progress{top:56px;left:0;right:0;height:3px;background:var(--line)}
.progress span{display:block;height:3px;background:var(--teal)}
.label{font-size:12px;color:var(--grey)}
.small{font-size:11px;line-height:13px;color:#333}
.ring{position:absolute;border:1px solid var(--teal);border-radius:50%;display:flex;align-items:center;justify-content:center}
.ring.grey{border-color:#bbb}
.bar{position:absolute;left:0;right:0;bottom:0;height:39px;background:var(--teal);color:var(--white)}
.teal{color:var(--teal)}
/* login */
.login-photo{position:absolute;inset:0;background:linear-gradient(135deg,#9fb8b3 0%,#6f8e8a 40%,#b9a79a 70%,#5e7e7c 100%)}
.login-shade{position:absolute;inset:0;background:linear-gradient(180deg,rgba(51,184,164,.25) 0%,rgba(51,184,164,.55) 45%,#11b09a 85%,#0aa891 100%)}
.field{position:absolute;left:20px;width:237px;height:36px;background:rgba(255,255,255,.18);color:var(--white);font-size:13px;display:flex;align-items:center;justify-content:center}
.btn{position:absolute;height:36px;font-size:13px;display:flex;align-items:center;justify-content:center}
.stepper{position:absolute;top:280px;width:44px;height:80px;border:1px solid #ddd;text-align:center}
.stepper .num{position:absolute;left:0;right:0;top:29px;font-size:16px}
</style>
</head>
<body>

<!-- Login -->
<section class="screen" style="left:21px;top:42px">
  <div class="login-photo" role="img" aria-label="Photo of a group of friends laughing together outdoors"></div>
  <div class="login-shade"></div>
  <div class="status" style="color:#fff"><span>●●●●● NetLine</span><span class="time">9:41 AM</span><span>100% ▬</span></div>
  <div class="abs" style="left:88px;top:45px;width:97px;height:97px;border-radius:50%;background:#fff"></div>
  <p class="abs center" style="top:155px;color:#fff;font-size:14px;line-height:18px">Leave the laundry to us,<br>you go out and have some fun!</p>
  <div class="field" style="top:243px">Username</div>
  <div class="field" style="top:288px">Password</div>
  <p class="abs" style="left:26px;top:339px;color:#fff;font-size:11px">Forgot password?</p>
  <div class="btn" style="left:18px;top:386px;width:113px;background:rgba(255,255,255,.3);color:#fff">Login</div>
  <div class="btn" style="left:145px;top:386px;width:112px;background:#fff;color:var(--teal)">Register</div>
  <p class="abs center" style="top:448px;font-size:10px;color:#fff">I am agree to <span style="color:#1a7d70">terms and conditions</span></p>
</section>

<!-- Empty order -->
<section class="screen" style="left:315px;top:42px">
  <div class="status"><span>●●●●● NetLine</span><span class="time">9:41 AM</span><span>100% ▬</span></div>
  <svg class="abs" style="left:0;top:24px" width="275" height="36" viewBox="0 0 275 36" fill="none" stroke-width="1.3">
    <g stroke="#04a690"><rect x="19" y="5" width="12" height="15" rx="1"/><path d="M22 5v4h6V5M25 9v11"/></g>
    <g stroke="#666"><path d="M66 12l8-8h7v7l-8 8z"/><circle cx="77.5" cy="7.5" r="1"/>
    <rect x="114" y="6" width="17" height="13" rx="1"/><path d="M114 10h17M125 13h6"/>
    <circle cx="171" cy="12.5" r="3"/><circle cx="171" cy="12.5" r="7.5" stroke-dasharray="3 1.7"/></g>
    <circle cx="254" cy="13" r="11" fill="#7a8c99" stroke="none"/>
  </svg>
  <div class="progress" style="top:57px;height:2px"><span style="width:50px;height:2px"></span></div>
  <svg class="abs" style="left:116px;top:140px" width="42" height="50" viewBox="0 0 42 50" fill="none" stroke="#888" stroke-width="1.4">
    <rect x="1" y="1" width="40" height="48" rx="2"/><path d="M1 11h40"/><circle cx="10" cy="6" r="1.5"/><circle cx="17" cy="6" r="1.5"/><circle cx="24" cy="6" r="1.5"/><circle cx="31" cy="6" r="1.5"/>
    <circle cx="21" cy="29" r="12"/><circle cx="21" cy="29" r="7" fill="#888"/>
  </svg>
  <h2 class="abs center" style="top:260px;font-size:17px;font-weight:400;color:#333">Empty Order</h2>
  <p class="abs center" style="top:300px;font-size:13px;line-height:16px;color:#888;padding:0 35px">Seems like you dont have any order yet. To make an order, press order button below</p>
  <div class="btn" style="left:17px;top:427px;width:240px;background:var(--teal);color:#fff">Start Order</div>
</section>

<!-- Schedule pick up -->
<section class="screen" style="left:609px;top:42px">
  <div class="status"><span>●●●●● NetLine</span><span class="time">9:41 AM</span><span>100% ▬</span></div>
  <svg class="abs close" width="14" height="14" stroke="#04a690" stroke-width="1.6"><path d="M1 1l12 12M13 1L1 13"/></svg>
  <p class="abs center header-title">Schedule Pick Up</p>
  <div class="progress"><span style="width:90px"></span></div>
  <p class="abs label" style="left:25px;top:80px">Where ?</p>
  <div class="ring" style="left:24px;top:103px;width:36px;height:36px">
    <svg width="14" height="18" fill="none" stroke="#04a690"><rect x="1" y="1" width="12" height="16"/><path d="M4 4h2M8 4h2M4 8h2M8 8h2M4 12h2M8 12h2"/></svg></div>
  <p class="abs small" style="left:75px;top:109px">Residence Kenanga Asri, Lt. 5,<br>No.120, Jakarta Pusat</p>
  <div class="ring grey" style="left:24px;top:149px;width:36px;height:36px">
    <svg width="18" height="18" stroke="#666"><path d="M9 1v16M1 9h16"/></svg></div>
  <p class="abs" style="left:75px;top:160px;font-size:10.5px;color:#aaa;font-style:italic;font-weight:300">Add new address</p>
  <p class="abs label" style="left:25px;top:210px">When ?</p>
  <div class="ring grey" style="left:24px;top:250px;width:36px;height:36px"><svg width="10" height="14" fill="none" stroke="#999"><path d="M8 1L2 7l6 6"/></svg></div>
  <div class="ring" style="left:214px;top:250px;width:36px;height:36px"><svg width="10" height="14" fill="none" stroke="#04a690"><path d="M2 1l6 6-6 6"/></svg></div>
  <p class="abs center" style="top:238px;font-size:32px;font-weight:300">29</p>
  <p class="abs center" style="top:284px;font-size:11px;color:#555">Friday</p>
  <p class="abs center" style="top:315px;font-size:12px;color:var(--grey)">At</p>
  <div class="ring grey" style="left:24px;top:331px;width:36px;height:36px"><svg width="10" height="14" fill="none" stroke="#999"><path d="M8 1L2 7l6 6"/></svg></div>
  <div class="ring" style="left:214px;top:331px;width:36px;height:36px"><svg width="10" height="14" fill="none" stroke="#04a690"><path d="M2 1l6 6-6 6"/></svg></div>
  <p class="abs center" style="top:341px;font-size:13px">10:00 to 10:30 AM</p>
  <p class="abs center" style="top:408px;font-size:8px;color:#aaa;font-style:italic">Note? e.g. will be handed over by maid</p>
  <div class="bar"><svg class="abs" style="right:34px;top:13px" width="18" height="14" fill="none" stroke="#fff" stroke-width="1.4"><path d="M0 7h17M11 1l6 6-6 6"/></svg></div>
</section>

<!-- Select services -->
<section class="screen" style="left:903px;top:42px">
  <div class="status"><span>●●●●● NetLine</span><span class="time">9:41 AM</span><span>100% ▬</span></div>
  <svg class="abs close" width="14" height="14" stroke="#04a690" stroke-width="1.6"><path d="M1 1l12 12M13 1L1 13"/></svg>
  <p class="abs center header-title">Select Services</p>
  <div class="progress"><span style="width:183px"></span></div>
  <div class="ring" style="left:30px;top:83px;width:36px;height:36px;border-width:1.5px;font-size:19px;font-weight:300;color:var(--teal)">3d</div>
  <div class="ring grey" style="left:119px;top:83px;width:36px;height:36px;border-color:#777;font-size:19px;font-weight:300">2d</div>
  <div class="ring grey" style="left:209px;top:83px;width:36px;height:36px;border-color:#777;font-size:19px;font-weight:300">1d</div>
  <p class="abs teal" style="left:28px;top:132px;font-size:11px;width:40px;text-align:center">Regular</p>
  <p class="abs" style="left:112px;top:132px;font-size:11px;width:50px;text-align:center">Express</p>
  <p class="abs" style="left:204px;top:132px;font-size:11px;width:46px;text-align:center">Deluxe</p>
  <p class="abs center label" style="top:174px">Select Item</p>
  <div class="ring" style="left:31px;top:207px;width:34px;height:34px"><svg width="14" height="14" fill="none" stroke="#04a690" stroke-width=".9"><rect x="1" y="3" width="12" height="10"/><path d="M5 3V1h4v2"/><text x="3.5" y="10.5" font-size="5" fill="#04a690" stroke="none">Kg</text></svg></div>
  <div class="ring" style="left:120px;top:207px;width:34px;height:34px"><svg width="18" height="12" fill="none" stroke="#04a690"><path d="M9 4a2 2 0 1 0-2-2M9 4v1L1 10h16L9 5"/></svg></div>
  <div class="ring grey" style="left:210px;top:207px;width:34px;height:34px;border-color:#777"><svg width="14" height="16" fill="none" stroke="#555"><rect x="1" y="1" width="12" height="14"/><path d="M1 4h12"/><circle cx="7" cy="9.5" r="3"/><circle cx="7" cy="9.5" r="1.3" fill="#555"/></svg></div>
  <p class="abs teal" style="left:23px;top:254px;font-size:11px;width:50px;text-align:center">Kg/s</p>
  <p class="abs teal" style="left:112px;top:254px;font-size:11px;width:50px;text-align:center">Pc/s</p>
  <p class="abs" style="left:199px;top:254px;font-size:11px;width:56px;text-align:center">Dry Clean</p>
  <div class="stepper" style="left:24px"><svg class="abs" style="left:15px;top:11px" width="14" height="8" fill="none" stroke="#ccc"><path d="M1 7l6-6 6 6"/></svg><span class="num teal">4</span><svg class="abs" style="left:15px;top:62px" width="14" height="8" fill="none" stroke="#ccc"><path d="M1 1l6 6 6-6"/></svg></div>
  <div class="stepper" style="left:115px"><svg class="abs" style="left:15px;top:11px" width="14" height="8" fill="none" stroke="#ccc"><path d="M1 7l6-6 6 6"/></svg><span class="num teal">8</span><svg class="abs" style="left:15px;top:62px" width="14" height="8" fill="none" stroke="#ccc"><path d="M1 1l6 6 6-6"/></svg></div>
  <div class="stepper" style="left:205px"><svg class="abs" style="left:15px;top:11px" width="14" height="8" fill="none" stroke="#ccc"><path d="M1 7l6-6 6 6"/></svg><span class="num">0</span><svg class="abs" style="left:15px;top:62px" width="14" height="8" fill="none" stroke="#ccc"><path d="M1 1l6 6 6-6"/></svg></div>
  <p class="abs" style="left:6px;top:375px;width:80px;text-align:center;font-size:11px;line-height:13px">Subtotal<br><span class="teal">IDR 120.000</span></p>
  <p class="abs" style="left:97px;top:375px;width:80px;text-align:center;font-size:11px;line-height:13px">Subtotal<br><span class="teal">IDR 200.000</span></p>
  <p class="abs" style="left:187px;top:375px;width:80px;text-align:center;font-size:11px;line-height:13px">Subtotal<br><span class="teal">IDR 0</span></p>
  <p class="abs label" style="left:18px;top:419px">Total Charge</p>
  <p class="abs teal" style="right:18px;top:419px;font-size:12px">Rp. 320.000,00</p>
  <div class="bar"><svg class="abs" style="right:34px;top:13px" width="18" height="14" fill="none" stroke="#fff" stroke-width="1.4"><path d="M0 7h17M11 1l6 6-6 6"/></svg></div>
</section>

<!-- Order summary -->
<section class="screen" style="left:21px;top:544px">
  <div class="status"><span>●●●●● NetLine</span><span class="time">9:41 AM</span><span>100% ▬</span></div>
  <svg class="abs close" width="14" height="14" stroke="#04a690" stroke-width="1.6"><path d="M1 1l12 12M13 1L1 13"/></svg>
  <p class="abs center header-title">Order Summary</p>
  <div class="progress" style="background:linear-gradient(90deg,var(--teal),var(--blue))"></div>
  <p class="abs" style="left:24px;top:77px;font-size:10.5px;color:var(--grey)">Pick Up</p>
  <div class="ring" style="left:24px;top:95px;width:36px;height:36px">
    <svg width="14" height="18" fill="none" stroke="#04a690"><rect x="1" y="1" width="12" height="16"/><path d="M4 4h2M8 4h2M4 8h2M8 8h2M4 12h2M8 12h2"/></svg></div>
  <p class="abs small" style="left:75px;top:102px">Residence Kenanga Asri, Lt. 5,<br>No.120, Jakarta Pusat</p>
  <p class="abs" style="left:75px;top:141px;font-size:10.5px;line-height:13px;color:var(--grey)">Friday, 29 January 2016<br>18:00 - 20:00 PM</p>
  <p class="abs" style="left:24px;top:182px;font-size:10.5px;color:var(--grey)">Services</p>
  <div class="ring" style="left:24px;top:202px;width:38px;height:38px;font-size:20px;font-weight:300;color:var(--teal)">3d</div>
  <p class="abs teal" style="left:75px;top:205px;font-size:11px">Regular</p>
  <p class="abs small" style="left:75px;top:221px">4 Kg/s Wash</p>
  <p class="abs small" style="right:23px;top:221px">Rp. 200.000,00</p>
  <div class="ring" style="left:24px;top:254px;width:38px;height:38px;font-size:20px;font-weight:300;color:var(--teal)">2d</div>
  <p class="abs teal" style="left:75px;top:257px;font-size:11px">Express</p>
  <p class="abs small" style="left:75px;top:274px">8 Pc/s Wash</p>
  <p class="abs small" style="right:23px;top:274px">Rp. 120.000,00</p>
  <p class="abs" style="left:24px;top:327px;font-size:10.5px;color:var(--grey)">Return</p>
  <p class="abs" style="left:23px;top:351px;font-size:17px;line-height:20px;font-weight:300;color:#222">Friday, 05 February 2015<br>07:00-08:00 PM</p>
  <p class="abs" style="left:25px;top:400px;font-size:10.5px;line-height:13px;color:#aaa">You can still modify return date/time<br>later in order tracking menu.</p>
  <div class="bar"><span class="abs" style="left:23px;top:13px;font-size:12px;font-weight:500">Rp. 320.000,00</span><span class="abs" style="right:23px;top:13px;font-size:12px;font-weight:500">Confirm</span></div>
</section>

</body>
</html>
```